Brindle Supports

We need an updated website that captures the comprehensive services and supports we provide to persons with developmental disabilities. We need a website design that educates families about the services we provide. We would also need a website that is user-friendly so that we could periodically update training schedules and ongoing programming.

• Thank you for submitting designs.  A few things I am hoping to see offered in the website:
• Front page highlights the services we offer (host homes, family caregiver, day program, employment program, SLS program, supported apartment program, behavior/clinical program)
• Front page also highlights any new programs we want to make prominent:  family caregiver, future restaurant employment openings, etc...
• Interactive Training Calendar
• Employee Resources page (link to carvix, email login, etc.)
• Uniform provider application for host home providers
• Information on agency - history, goals, etc.
• Contact Information/Location

 

Fun things to include:

• Client Highlights (featuring a client story each month, etc...)
• Employee highlights (featuring a staff member...)
• link to other Brindle business pages (Brindle Therapy and Brindle Restaurant)

```html
<!DOCTYPE html>
<html lang="en">
<head>
<meta charset="utf-8">
<title>Brindle Supports</title>
<link href="https://fonts.googleapis.com/css2?family=Bitter:wght@400;500;600&family=Arimo:wght@400;700&display=swap" rel="stylesheet">
<style>
:root{
  --maroon:#862f30;
  --maroon-dark:#6e2425;
  --orange:#e06a12;
  --ink:#1d1d1d;
  --grey-icon:#4a4a4a;
  --panel:#e7e1e3;
  --panel-line:#c9c3c5;
  --nav-top:#f1eff0;
  --nav-bottom:#d6d2d4;
  --white:#ffffff;
}
*{box-sizing:border-box;margin:0;padding:0}
html,body{width:1159px;height:1200px;overflow:hidden;background:var(--white)}
body{position:relative;font-family:"Arimo",Arial,sans-serif;color:var(--ink)}
.abs{position:absolute}
.brand{left:96px;top:40px;display:flex;align-items:center;gap:14px}
.brand-dot{width:44px;height:44px;border-radius:50%;background:var(--maroon)}
.brand-name{font-family:"Bitter",Georgia,serif;font-weight:600;font-size:40px;color:var(--ink);letter-spacing:1px}
.tagline{left:61px;top:134px;font-family:"Bitter",Georgia,serif;font-size:11.5px;letter-spacing:.3px;color:var(--ink)}
.contact-line{left:679px;top:26px;font-size:16px;color:var(--maroon)}
.contact-line .num{font-size:21px;color:var(--ink);margin:0 14px 0 3px}
.social{top:16px;width:36px;height:36px;background:var(--grey-icon)}
.host-btn{left:891px;top:79px;width:214px;height:50px;background:var(--orange);color:var(--white);font-family:"Bitter",Georgia,serif;font-weight:600;font-size:16.5px;display:flex;align-items:center;justify-content:center;border-radius:3px;box-shadow:0 6px 6px -4px rgba(0,0,0,.25)}
.nav{left:0;top:156px;width:1159px;height:51px;background:linear-gradient(var(--nav-top),var(--nav-bottom))}
.nav a{position:absolute;top:0;height:51px;line-height:51px;font-family:"Bitter",Georgia,serif;font-weight:500;font-size:15px;color:var(--ink);text-decoration:none}
.nav a.active{background:var(--maroon);color:var(--white);width:129px;text-align:center;font-weight:600}
.dropdown{left:229px;top:207px;width:212px;height:145px;background:var(--maroon);padding:20px 16px}
.dropdown a{display:block;font-family:"Bitter",Georgia,serif;font-size:13.5px;color:var(--white);text-decoration:none;margin-bottom:15px}
.dropdown a.current{border-bottom:1px solid rgba(255,255,255,.7);padding-bottom:3px;width:135px;margin-bottom:12px}
.hero{left:45px;top:217px;width:1071px;height:457px;background:linear-gradient(100deg,#4f6b45 0%,#6f8c5a 22%,#c9a98f 40%,#e8dccd 58%,#9fb88a 80%,#3c4a3c 100%);overflow:hidden}
.hero-arrow{top:160px}
.caption{left:46px;top:241px;width:386px;height:188px;background:rgba(255,255,255,.45);padding:12px 14px;font-family:"Bitter",Georgia,serif;font-size:34px;line-height:41px;color:var(--ink)}
.caption svg{vertical-align:-6px;margin-left:4px}
h2{font-family:"Bitter",Georgia,serif;font-weight:500;font-size:21px;color:var(--maroon)}
.copy{font-size:14px;line-height:20.5px;text-align:justify}
.welcome{left:54px;top:706px;width:357px}
.mission{left:50px;top:901px;width:357px}
.welcome h2,.mission h2{margin-bottom:8px}
.training{left:435px;top:708px;width:340px}
.event{position:absolute;left:-3px;width:340px}
.date{position:absolute;left:0;top:0;width:57px;height:54px;background:var(--maroon);color:var(--white);font-size:15px;line-height:17px;text-align:center;padding-top:9px}
.event-title{position:absolute;left:80px;top:0;font-size:17px}
.event-text{position:absolute;left:80px;top:25px;width:255px;font-size:13.5px;line-height:16px}
.side-box{left:793px;width:310px;background:var(--panel);border:1px solid var(--panel-line);padding:12px 24px}
.side-box ul{list-style:none;margin-top:8px}
.side-box li{font-size:14.5px;font-weight:700;letter-spacing:.4px;line-height:27px;padding-left:20px;position:relative}
.side-box li::before{content:"";position:absolute;left:2px;top:11px;width:6px;height:6px;border-radius:50%;background:var(--ink)}
.footer{left:0;top:1074px;width:1159px;height:126px;background:var(--maroon);color:var(--white)}
.footer h3{position:absolute;left:67px;top:20px;font-family:"Bitter",Georgia,serif;font-weight:500;font-size:20px}
.footer p{position:absolute;left:66px;font-size:14px}
.footer .legal{left:auto;right:76px;top:100px;font-size:11.5px}
</style>
</head>
<body>
<header>
  <div class="abs brand"><span class="brand-dot"></span><span class="brand-name">Brindle Supports</span></div>
  <div class="abs tagline">BUILDING ABILITIES | CREATING OPPORTUNITIES | DEVELOPING RELATIONSHIPS</div>
  <div class="abs contact-line">Call us <span class="num">720 5550148</span> Connect with us</div>
  <span class="abs social" style="left:1014px" aria-label="Social link"></span>
  <span class="abs social" style="left:1057px" aria-label="Social link"></span>
  <a class="abs host-btn">Become a&nbsp; Host Provider</a>
</header>
<nav class="abs nav">
  <a style="left:54px">Home</a>
  <a style="left:125px">Our Services</a>
  <a class="active" style="left:229px">Our Program</a>
  <a style="left:370px">Employee Resources</a>
  <a style="left:548px">Community Resources</a>
  <a style="left:742px">Our Team</a>
  <a style="left:841px">Calender</a>
  <a style="left:934px">Location</a>
  <a style="left:1025px">Contact us</a>
</nav>
<section class="abs hero" role="img" aria-label="Photo of a caregiver smiling beside a young boy stacking coloured building blocks">
  <svg class="abs hero-arrow" style="left:20px" width="36" height="72" viewBox="0 0 36 72"><polyline points="34,2 2,36 34,70" fill="none" stroke="#222" stroke-width="1.5"/></svg>
  <svg class="abs hero-arrow" style="right:8px" width="36" height="72" viewBox="0 0 36 72"><polyline points="2,2 34,36 2,70" fill="none" stroke="#222" stroke-width="1.5"/></svg>
  <div class="abs caption">Praesent vestibulum molestie lacus enean nonummy hendrerit<svg width="28" height="38" viewBox="0 0 28 38"><polygon points="0,0 28,19 0,38" fill="var(--maroon)"/></svg></div>
</section>
<div class="abs dropdown">
  <a class="current">Residential Program</a>
  <a>Day.Employment Program</a>
  <a>SLS Program</a>
</div>
<section class="abs welcome">
  <h2>Welcome</h2>
  <p class="copy"><b>Brindle Supports</b> is an agency designed to creatively serve individuals with developmental disabilities in community-based settings throughout Colorado. Brindle Supports is an approved service agency through the Division of Developmental Disabilities.</p>
</section>
<section class="abs mission">
  <h2>Our Misson</h2>
  <p class="copy">To promote relationships, attachment, positive boundaries, and resource development to create opportunities and improve the lives of people living with disabilities.</p>
</section>
<section class="abs training">
  <h2>Upcoming Training Schedule</h2>
  <div class="event" style="top:55px">
    <div class="date">15<br>April</div>
    <div class="event-title">Praesent vestibulum molestie</div>
    <div class="event-text">Praesent vestibulum molestie lacus enean nonummy hendrerit maurisem. Phasellus porta.</div>
  </div>
  <div class="event" style="top:177px">
    <div class="date">19<br>April</div>
    <div class="event-title" style="left:76px">Praesent vestibulum molestie</div>
    <div class="event-text" style="left:76px">Praesent vestibulum molestie lacus enean nonummy hendrerit maurisem. Phasellus porta.</div>
  </div>
</section>
<aside class="abs side-box" style="top:698px;height:156px">
  <h2>Our Programs</h2>
  <ul><li>Residential Program</li><li>Day/Employment Program</li><li>SLS Program</li></ul>
</aside>
<aside class="abs side-box" style="top:867px;height:159px">
  <h2>Client Support</h2>
  <ul><li>Integrated Treatment Plans</li><li>Behavioral Supports</li><li>Agency Sponsered Activities</li></ul>
</aside>
<footer class="abs footer">
  <h3>Brindle Supports</h3>
  <p style="top:54px">418 Alder Lane ~ Fairview, CO 80599</p>
  <p style="top:76px">Phone: 720-555-0148&nbsp; Fax: 303-555-0172</p>
  <p class="legal">Content copyright 2014. Brindle Supports. All rights reserved.</p>
</footer>
</body>
</html>
```